Univ of Westbrook disability insurance program

We are an endorsed vendor for disability insurance the the University of Westbrook. We work together with the University to promote this program. They send emails on our behalf but we send some too. I'm not confident the emails we send are as effective as they could be. I have attached examples of 2 versions of the same email we send students and residents. I would love your opinion on how to make these better and shorter. They are emails, not brochures. I have several others but starting with these. I would like to see consistency in all the pieces we email to the students and residents. I also feel like we have to many words in our pieces and they could be shortened up with better word smithing. Once we settle on a design of these emails and better wording I have about 5 other emails I would like to have looked at to coordinate with the one we are doing now. In each of these programs at the University we have an assigned Dunmore Vance representative. We do want to add their pictures to these too as one of the examples has.
Updates

I forgot to mention that I need both logo's in the email. The Dunmore Vance logo and the University of Westbrook Office of Student Health Benefits logo. Do you need an electronic version of the email? Let me know. Thanks

Target Market(s)

students and medical residents

Industry/Entity Type

Insurance

Font styles to use
Sans Serif

Requirements
Must have
• Short and worded to the point
• Can use maroon and gold coloring
Nice to have
• Easier to read
Should not have
• Walls of words as students and residents dont have a lot of extra time on their hands.

```html
<!DOCTYPE html>
<html lang="en">
<head>
<meta charset="utf-8">
<title>Dunmore Vance – Disability Insurance for Completing Students</title>
<link rel="stylesheet" href="https://fonts.googleapis.com/css2?family=Lato:wght@400;700&family=Oswald:wght@500;700&display=swap">
<style>
  :root{
    --maroon:#7a0019;
    --gold:#ffcc33;
    --ink:#1e1e1e;
    --navy:#1f2f6b;
    --page:#d6d6d6;
    --paper:#f4f4f4;
  }
  *{box-sizing:border-box;margin:0;padding:0}
  html,body{width:1200px;height:1200px;overflow:hidden}
  body{background:var(--page);font-family:"Lato",sans-serif;color:var(--ink);position:relative}
  .flyer{position:absolute;left:219px;top:66px;width:762px;height:1069px;background:var(--paper);overflow:hidden;box-shadow:0 12px 24px rgba(0,0,0,.25)}
  .header{position:absolute;left:0;top:0;width:100%;height:170px;background:var(--gold)}
  .header-stripe{position:absolute;left:0;top:139px;width:100%;height:12px;background:var(--maroon)}
  .brand{position:absolute;display:flex;align-items:center;gap:10px}
  .brand-left{left:32px;top:60px}
  .brand-left .mark{width:50px;height:50px;border-radius:50%;background:var(--navy)}
  .brand-left .name{font-size:26px;font-weight:400;color:var(--navy);letter-spacing:1px}
  .brand-right{right:36px;top:56px}
  .brand-right .mark{width:46px;height:46px;background:var(--maroon)}
  .brand-right .name{font-size:14px;font-weight:700;color:var(--maroon);line-height:1.5}
  .hero-photo{position:absolute;left:0;top:170px;width:100%;height:307px;background:linear-gradient(90deg,#e8edf1 0%,#f7f8f9 45%,#f3efe9 100%)}
  .hero-portrait{position:absolute;left:322px;top:52px;width:130px;height:118px;background:linear-gradient(180deg,#f5f3ef,#ffcc33);}
  .title-band{position:absolute;left:0;top:477px;width:100%;height:146px;background:var(--maroon);text-align:center;font-family:"Oswald",sans-serif;font-weight:700;text-transform:uppercase}
  .title-band .kicker{display:block;color:#fff;font-size:54px;line-height:1;margin-top:20px;font-weight:500}
  .title-band .headline{display:block;color:var(--gold);font-size:52px;line-height:1;margin-top:4px;text-shadow:2px 2px 0 rgba(0,0,0,.35)}
  .letter{position:absolute;left:31px;top:632px;width:705px;font-size:11px;line-height:1.25}
  .letter .salutation{font-size:14px;margin-bottom:6px}
  .letter h2{font-size:17px;font-weight:700;margin:0 0 6px}
  .letter p{margin-bottom:10px}
  .letter h2.spaced{margin-top:4px}
  .reasons{list-style:none;margin:10px 0 8px}
  .reasons li{position:relative;padding-left:14px;margin-bottom:6px}
  .reasons li::before{content:"";position:absolute;left:2px;top:4px;width:4px;height:4px;border-radius:50%;background:var(--maroon)}
  .footer{position:absolute;left:0;top:1009px;width:100%;height:60px;background:var(--gold)}
  .footer-shape{position:absolute;left:0;top:0}
  .contact{position:absolute;top:0;height:60px;display:flex;align-items:center;gap:8px;font-size:11px}
  .contact svg{flex:none}
  .contact.phone{left:52px;color:#fff;font-size:14px;font-weight:700}
  .contact.email{left:256px;color:#fff}
  .contact.web{left:530px;color:var(--ink)}
</style>
</head>
<body>
<main class="flyer">
  <header class="header">
    <div class="header-stripe"></div>
    <div class="brand brand-left">
      <span class="mark"></span>
      <span class="name">DUNMORE VANCE</span>
    </div>
    <div class="brand brand-right">
      <span class="mark"></span>
      <span class="name">Student Health Benefits<br>University of Westbrook</span>
    </div>
  </header>

  <div class="hero-photo" role="img" aria-label="Photo of smiling young doctors in white coats, a man with a stethoscope in front, arms crossed"></div>

  <section class="title-band">
    <span class="kicker">Attention:</span>
    <span class="headline">Completing Students</span>
  </section>

  <section class="letter">
    <p class="salutation">Dear John,</p>
    <h2>Finally. It’s Your Time</h2>
    <p>You’re close to reaping the rewards of all the hard work and sacrifices you’ve made to get where you are now.</p>
    <h2 class="spaced">But What Would Happen If You Became Too Sick or Injured to Work?</h2>
    <p>Even with health care costs paid by insurance, you’d still need funds for food, rent, utilities, cell phone, etc. Not only is your income essential for your daily living expenses, but also to repay student loans. Disability Income insurance (DI) can help by replacing part of your income to help you cover these critical expenses.</p>
    <h2 class="spaced">Why Consider Disability Insurance Now:</h2>
    <ul class="reasons">
      <li>SPECIALTY LANGUAGE: Coverage to protect you in your own occupation or your specialty.</li>
      <li>STUDENT LOAN PROTECTION: Option to cover your student loan debt.</li>
      <li>HEALTH: Your eligibility for disability insurance and your ability to obtain it on the most favorable terms depend on your health.</li>
      <li>COST: The cost of DI protection is age-based. Lock in a lower rate by applying while you’re young.</li>
      <li>NO PROOF OF EARNINGS REQUIRED: For eligible occupations, our Program for New Young Professionals<br>provides a monthly benefit based on the earnings you expect early in your career – without proof of income.</li>
      <li>PORTABILITY: You’ll likely change employers during your working life. Group LTD is typically not portable,<br>you’ll want to consider having individual disability coverage that is with you regardless of employer.</li>
    </ul>
    <p>Take advantage of this opportunity now to obtain industry-leading coverage to protect your income and future. Don’t forget, you have access to a <strong>GUARANTEED ISSUE</strong> plan as a completing student!</p>
  </section>

  <footer class="footer">
    <svg class="footer-shape" width="762" height="60" viewBox="0 0 762 60" aria-hidden="true">
      <polygon points="0,0 482,0 442,60 0,60" fill="var(--maroon)"/>
      <polygon points="486,0 490,0 450,60 446,60" fill="#fff"/>
    </svg>
    <div class="contact phone">
      <svg width="18" height="18" viewBox="0 0 18 18" aria-hidden="true"><circle cx="9" cy="9" r="8" fill="none" stroke="#fff" stroke-width="1.5"/><path d="M6 5l2 2-1 1.3c.6 1.3 1.5 2.2 2.7 2.7L11 10l2 2-1.2 1.3C8.5 13 5 9.5 4.7 6.2z" fill="#fff"/></svg>
      <span>(555)318-4720</span>
    </div>
    <div class="contact email">
      <svg width="18" height="13" viewBox="0 0 18 13" aria-hidden="true"><rect x=".75" y=".75" width="16.5" height="11.5" fill="none" stroke="#fff" stroke-width="1.5"/><path d="M1 1l8 6 8-6M1 12l6-5M17 12l-6-5" fill="none" stroke="#fff" stroke-width="1.2"/></svg>
      <span>dana_hollis@dunmorevance.com</span>
    </div>
    <div class="contact web">
      <svg width="18" height="18" viewBox="0 0 18 18" aria-hidden="true"><g fill="none" stroke="#1e1e1e" stroke-width="1.3"><circle cx="9" cy="9" r="8"/><ellipse cx="9" cy="9" rx="3.5" ry="8"/><path d="M1 9h16M2.5 5h13M2.5 13h13"/></g></svg>
      <span>www.uwbdisabilitybenefits.com</span>
    </div>
  </footer>
</main>
</body>
</html>
```